Logo and metal business card design

Updated added my current logo which focus needs to be concentrated on. Have to have the new logo before the card. Company name is The Halden Crest, LLC

Update: Reminder this is a Logo and business card design. I want the logo to be “HaldenC” in a unique professional design that says secure, insurance, financial.

The G needs to be a P in the cut out

Update: the top two images have design on the metal which I am looking for

New black metal business cards. And HaldenC.com logo that will go on the card. This will be a cut out design in the metal. Featuring “HaldenC.com as the main cutout. Like the idea of .com to be separate or smaller and possible color. Looking for unique HaldenC font design and a surrounding design per the examples below. Halden and G need to be different and the G a specific designing the mesh like the attached with the V in the mesh. But card side ways.. so mesh on right side of card with a G and .com in lower corner or where it fits Also looking to add my main info on the back side of the card. Derek M. Cell contact@mailbox-example.net We are an commercial insurance broker specializing in program business.

Need more time not enough entry’s and they are all the same.. I’m suppose to get 75 plus and not 20 that are the exact same from artist??? Need more submissions to compare. I committed my money so I do not want a refund I want more submissions from different artist

Designs look the same

Target Market(s)

Insurance for the Restaurant industry

Industry/Entity Type

Insurance Broker

Contact Information for Business Card

New black metal business cards. And HaldenC.com logo that will go on the card. This will be a cut out design in the metal. Featuring “HaldenC.com as the main cutout. Like the idea of .com to be separate or smaller and possible color. Looking for unique HaldenC font design and a surrounding design per the examples below. Halden and G need to be different and the G a specific designing the mesh like the attached with the V in the mesh. But card side ways.. so mesh on right side of card with a G and .com in lower corner or where it fits
Also looking to add my main info on the back side of the card.
Derek M.
Cell
contact@mailbox-example.net

We are an commercial insurance broker specializing in program business.

Logo Text

HaldenC.com

Font styles to use
Decorative
Script
Other font styles liked:

Requirements
Must have
• Must have Halden and G distinctively different
Nice to have
• On flat parts I want texture on top of card

```html
<!DOCTYPE html>
<html lang="en">
<head>
<meta charset="utf-8">
<title>HaldenC Business Card</title>
<link href="https://fonts.googleapis.com/css2?family=Tinos:wght@700&family=Didact+Gothic&display=swap" rel="stylesheet">
<style>
  :root {
    --backdrop: #3a3b3d;
    --navy: #1f2e5f;
    --navy-ink: #23356b;
    --paper: #ffffff;
    --ink: #1b1b1f;
    --sky: #4fb0ea;
    --rule: #111111;
  }
  * { box-sizing: border-box; margin: 0; padding: 0; }
  html, body { width: 1200px; height: 960px; overflow: hidden; }
  body {
    background: var(--backdrop);
    display: flex;
    flex-direction: column;
    align-items: center;
    justify-content: center;
    gap: 48px;
  }
  .card {
    width: 660px;
    height: 378px;
    border-radius: 28px;
    position: relative;
    overflow: hidden;
  }
  .card--front { background: var(--navy); display: flex; align-items: center; justify-content: center; }
  .card--back { background: var(--paper); display: flex; align-items: center; }

  .brand { display: flex; align-items: center; gap: 12px; white-space: nowrap; }
  .brand__dot {
    width: 28px; height: 28px; border-radius: 50%;
    background: var(--sky);
    flex: none;
  }
  .brand__name {
    font-family: "Tinos", serif;
    font-weight: 700;
    font-size: 48px;
    letter-spacing: 1px;
  }
  .card--front .brand__name { color: var(--paper); }
  .card--back .brand__name { color: var(--navy-ink); }

  .back__logo {
    width: 48%;
    display: flex;
    justify-content: center;
  }
  .back__rule {
    width: 2px;
    height: 230px;
    background: var(--rule);
    flex: none;
  }
  .back__info { padding-left: 30px; padding-right: 20px; }
  .back__name {
    font-family: "Tinos", serif;
    font-weight: 700;
    font-size: 32px;
    color: var(--navy-ink);
    margin-bottom: 14px;
    white-space: nowrap;
  }
  .contact { list-style: none; font-family: "Didact Gothic", sans-serif; font-size: 17px; color: var(--ink); }
  .contact li { display: flex; align-items: flex-start; gap: 12px; line-height: 1.35; margin-bottom: 4px; white-space: nowrap; }
  .contact li.contact__address { margin-top: 12px; }
  .contact svg { width: 17px; height: 17px; flex: none; margin-top: 3px; fill: var(--navy-ink); }
</style>
</head>
<body>
  <section class="card card--front" aria-label="Card front">
    <div class="brand">
      <span class="brand__dot"></span>
      <span class="brand__name">HaldenC</span>
    </div>
  </section>

  <section class="card card--back" aria-label="Card back">
    <div class="back__logo">
      <div class="brand">
        <span class="brand__dot"></span>
        <span class="brand__name">HaldenC</span>
      </div>
    </div>
    <div class="back__rule"></div>
    <div class="back__info">
      <h1 class="back__name">Derek M.</h1>
      <ul class="contact">
        <li>
          <svg viewBox="0 0 24 24" aria-hidden="true"><path d="M6.6 10.8a15.1 15.1 0 0 0 6.6 6.6l2.2-2.2a1 1 0 0 1 1-.25 11.4 11.4 0 0 0 3.6.57 1 1 0 0 1 1 1V20a1 1 0 0 1-1 1A17 17 0 0 1 3 4a1 1 0 0 1 1-1h3.5a1 1 0 0 1 1 1c0 1.25.2 2.45.57 3.570a1 1 0 0 1-.25 1z"/></svg>
          <span>555-014-7300</span>
        </li>
        <li>
          <svg viewBox="0 0 24 24" aria-hidden="true"><path d="M2 5h20v14H2z M2 5l10 8 10-8" fill="none" stroke="#23356b" stroke-width="2"/><path d="M3 6l9 7 9-7v-1H3z"/></svg>
          <span>youremail@mailbox-example.net</span>
        </li>
        <li>
          <svg viewBox="0 0 24 24" aria-hidden="true"><circle cx="12" cy="12" r="9" fill="none" stroke="#23356b" stroke-width="2"/><path d="M3 12h18M12 3c3 3 3 15 0 18M12 3c-3 3-3 15 0 18" fill="none" stroke="#23356b" stroke-width="1.6"/></svg>
          <span>www.yourwebsite.com</span>
        </li>
        <li class="contact__address">
          <svg viewBox="0 0 24 24" aria-hidden="true"><path d="M12 2a7 7 0 0 0-7 7c0 5.2 7 13 7 13s7-7.8 7-13a7 7 0 0 0-7-7zm0 9.5A2.5 2.5 0 1 1 12 6.5a2.5 2.5 0 0 1 0 5z"/></svg>
          <span>Your address<br>city, state, ZIP 0000</span>
        </li>
      </ul>
    </div>
  </section>
</body>
</html>
```